International Digital Platform Startup needs powerpoint design

We need a powerpoint design for a new SaaS and platform startup based in Helsinki, Finland called Kelmora Ltd. We help companies to create, calculate and communicate customer value and capture that value into cashflow. Company owners, boards and management teams will use this platform and the digital tool to have a transparent customer value view. The digital tool helps everyone in the organisation to see how they can create value in their job.
Benefits of Bridges2ClientWorth - tool:
Emotional benefits:
- Helps me succeed
- I’m forerunner
- I’m up to date
- I accomplish
- process is under control
- Ease to lead
- Ease in communication

Rational benefits:
- Simplicity in complex world of value
- Clarity
- Easy access - low deployment threshold

The final design should express Kelmora's brand personality: Creative, Analytic, Curious, Trustworthy, Brave. Our color is green as seen in logos.
Updates

Hi, Thank you for everyone participating so far to design the powerpoint template for Kelmora. There are some essential emphasis I would like to point out to help you design for us: - Kelmora is the company name, and we are building the tool and the platform called Bridges2ClientWorth. The emphasis is on the Bridges2ClientWorth -logo thought the company name and logo Kelmora needs to be there. This is one of the most important parts of the design – it needs to work. Logos should also not been framed in anyway. - We don’t need that many different pages, but the ones that can be used for several purposes – Keep it simple. - Since we are a Finnish startup, we like to look like one. Visually that means highlighting Finnish and startup, both meaning for us o Nordic clarity and simplicity o Freshness o Nordic design - The green color in our logos is the company color – in our coming website we are also using more fresh, lighter “mint“ like color and white headings with Barlow bold and regular fonts. Since this font doesn't appear in microsoft powerpoint, please use some of the fonts that do. (it seems I'm not able to place a screenshot of our webpage here. I'll be happy to provide one for you if it needed. The webpage is not public yet) I hope to hear from you soon. I'm in need to use the powerpoint in about one week : ) Creating Value with You, Eeva

Hi, Kelmora website has now been published at kelmora-example.com. In english site, there might still be something that needs to be fixed, but I'm sure it will help you to succeed with your design proposal. if there is any additional information you would need for this work, please let me know. I would be more than happy to provide it for you. Eeva

```html
<!DOCTYPE html>
<html lang="en">
<head>
<meta charset="utf-8">
<title>Kelmora – Bridges2ClientWorth presentation template</title>
<link rel="stylesheet" href="https://fonts.googleapis.com/css2?family=Ubuntu:wght@300;400;500;700&family=Open+Sans:wght@400;600&display=swap">
<style>
  :root {
    --lime: #8cd614;
    --green: #22c31e;
    --green-soft: #4fcf4a;
    --mint: #ccf5cc;
    --forest: #1b7d1f;
    --haze: #e2e4ee;
    --ink: #111;
    --body: #444;
    --white: #fff;
  }
  * { box-sizing: border-box; margin: 0; padding: 0; }
  html, body { width: 900px; height: 1200px; overflow: hidden; background: var(--white); }
  .board {
    position: relative; width: 1680px; height: 2240px;
    transform: scale(0.535714); transform-origin: 0 0;
    font-family: "Open Sans", Arial, sans-serif; color: var(--body);
  }
  .slide {
    position: absolute; width: 557px; height: 314px; overflow: hidden;
    background: var(--white); box-shadow: 0 6px 18px rgba(0,0,0,.22);
  }
  .slide > * { position: absolute; }
  .col-l { left: 199px; } .col-r { left: 903px; }
  .row1 { top: 62px; } .row2 { top: 420px; } .row3 { top: 779px; }
  .row4 { top: 1138px; } .row5 { top: 1497px; } .row6 { top: 1856px; }

  .wordmark { font-family: "Ubuntu", sans-serif; font-weight: 400; color: var(--ink); font-size: 19px; letter-spacing: -.3px; }
  .wordmark.light { color: var(--white); }
  .corner-mark { right: 34px; top: 14px; }
  .heading { font-family: "Ubuntu", sans-serif; font-weight: 400; color: var(--green); font-size: 21px; line-height: 1.3; }
  .small { font-size: 5.5px; line-height: 1.9; color: var(--body); }
  .small.light { color: var(--white); }
  .fill-photo { }
  .bar { bottom: 0; height: 5px; }

  /* slide 1 */
  .cover-photo { left: 0; top: 0; width: 477px; height: 314px; background: linear-gradient(100deg, #fbfbfb 0%, #eef0f1 40%, #c9cdd0 70%, #8d9296 100%); }
  .cover-band { left: 477px; top: 0; width: 80px; height: 314px; background: var(--lime); }
  .cover-tag { left: 412px; top: 242px; width: 145px; height: 72px; background: var(--green); color: var(--white); font-size: 9.5px; line-height: 1.45; text-align: center; padding-top: 22px; }
  .cover-title { left: 77px; top: 86px; font-family: "Ubuntu", sans-serif; color: var(--ink); }
  .cover-title .wordmark { font-size: 42px; display: block; line-height: 1; }
  .cover-title .product { font-size: 28px; line-height: .98; letter-spacing: -1px; font-weight: 300; display: block; margin-top: 8px; }

  /* slide 2 */
  .runner-photo { left: 0; top: 0; width: 557px; height: 222px; background: linear-gradient(180deg, #dfe9f1 0%, #eef2f4 55%, #9aa1a6 85%, #6b7074 100%); }
  .intro-mark { left: 85px; top: 244px; font-size: 40px; }
  .intro-text { left: 238px; top: 246px; width: 228px; }

  /* slide 3 */
  .meeting-photo { left: 0; top: 0; width: 443px; height: 314px; background: linear-gradient(90deg, #d9d2c6 0%, #b9ad9c 50%, #6f6a62 100%); }
  .meeting-tint { left: 215px; top: 0; width: 228px; height: 314px; background: rgba(34,195,30,.72); }
  .meeting-veil { left: 103px; top: 58px; width: 340px; height: 200px; background: rgba(255,255,255,.62); }
  .hello-title { left: 163px; top: 112px; font-family: "Ubuntu", sans-serif; font-size: 20px; color: #333; }
  .hello-text { left: 163px; top: 146px; width: 230px; }
  .hello-vertical { left: 477px; top: 30px; writing-mode: vertical-rl; font-family: "Ubuntu", sans-serif; font-weight: 700; font-size: 36px; color: #eceef2; }

  /* slide 4 */
  .we-title { left: 58px; top: 66px; }
  .we-text { left: 58px; top: 100px; width: 208px; font-size: 6.2px; line-height: 1.55; color: #222; text-align: justify; }
  .we-text p + p { margin-top: 7px; text-align: left; }
  .leaf-photo { left: 297px; top: 0; width: 147px; height: 206px; background: linear-gradient(135deg, #8fb25d 0%, #5f8f3a 50%, #9cc06a 100%); }
  .water-photo { left: 297px; top: 206px; width: 147px; height: 108px; background: linear-gradient(180deg, #3fd6c8 0%, #5fe0d2 100%); }
  .we-band { left: 444px; top: 0; width: 113px; height: 314px; background: var(--green); }
  .we-mark { left: 460px; top: 14px; font-size: 20px; }
  .we-note1 { left: 466px; top: 94px; width: 70px; }
  .we-note2 { left: 466px; top: 250px; width: 70px; }

  /* slide 5 */
  .hands-photo { left: 0; top: 0; width: 557px; height: 314px; background: linear-gradient(90deg, #b7b7b2 0%, #e6e6e4 60%, #8f8f8c 100%); }
  .quote-band { left: 0; top: 0; width: 48px; height: 314px; background: var(--lime); }
  .quote-panel { left: 48px; top: 42px; width: 460px; height: 272px; background: rgba(140,214,20,.86); }
  .quote-lead { left: 108px; top: 96px; width: 230px; }
  .quote-text { left: 108px; top: 143px; width: 320px; font-family: "Ubuntu", sans-serif; font-size: 19px; line-height: 1.45; color: var(--white); }
  .quote-text b { font-weight: 700; }
  .quote-mark { left: 434px; top: 281px; font-size: 18px; }

  /* slide 6 */
  .profile-title { left: 53px; top: 46px; }
  .profile-text1 { left: 53px; top: 78px; width: 225px; }
  .profile-text2 { left: 350px; top: 78px; width: 170px; }
  .profile-block { left: 0; top: 156px; width: 116px; height: 158px; background: var(--green); }
  .desk-photo { left: 116px; top: 156px; width: 409px; height: 158px; background: linear-gradient(135deg, #6edc6a 0%, #4fcf4a 50%, #7be276 100%); }

  /* slide 7 */
  .tool-block { left: 0; top: 0; width: 195px; height: 222px; background: var(--green); }
  .tool-haze1 { left: 195px; top: 0; width: 33px; height: 254px; background: var(--haze); }
  .tool-haze2 { left: 0; top: 222px; width: 162px; height: 32px; background: var(--haze); }
  .class-photo { left: 49px; top: 45px; width: 146px; height: 177px; background: linear-gradient(180deg, #e8e4de 0%, #b9b2a8 55%, #3b3f4a 100%); }
  .laptop-photo { left: 162px; top: 124px; width: 117px; height: 146px; background: linear-gradient(160deg, #79e074 0%, #3bbf38 100%); }
  .tool-title { left: 326px; top: 54px; }
  .tool-list { left: 326px; top: 112px; width: 200px; }
  .tool-item { margin-bottom: 14px; }
  .tool-item h4 { font-family: "Ubuntu", sans-serif; font-weight: 400; font-size: 7px; letter-spacing: .5px; color: #555; margin-bottom: 4px; }

  /* slide 8 */
  .grey-photo { left: 0; top: 40px; width: 147px; height: 232px; background: linear-gradient(180deg, #9a9a9a 0%, #5d5d5d 60%, #2c2c2c 100%); }
  .green-photo { left: 147px; top: 40px; width: 297px; height: 232px; background: linear-gradient(135deg, #3fc93a 0%, #30b52c 100%); }
  .rational-mint { left: 444px; top: 40px; width: 113px; height: 232px; background: var(--mint); }
  .rational-title { left: 195px; top: 103px; color: var(--white); font-size: 21px; letter-spacing: .5px; }
  .rational-list { left: 195px; top: 136px; font-size: 9px; line-height: 2.3; color: var(--white); list-style: none; }

  /* slide 9 */
  .about-top { left: 372px; top: 0; width: 185px; height: 46px; background: var(--lime); }
  .about-mark { left: 460px; top: 14px; }
  .about-bottom { left: 372px; top: 268px; width: 185px; height: 46px; background: var(--lime); }
  .circle-photo { left: 278px; top: 46px; width: 279px; height: 222px; background: linear-gradient(120deg, #e9e9e9 0%, #b39585 45%, #5a4a40 100%); }
  .about-title { left: 32px; top: 90px; font-size: 20px; }
  .about-text { left: 32px; top: 124px; width: 228px; text-align: justify; }

  /* slide 10 */
  .value-mint { left: 0; top: 0; width: 337px; height: 314px; background: var(--mint); }
  .value-band { left: 337px; top: 0; width: 220px; height: 314px; background: var(--green); }
  .shop-photo { left: 0; top: 42px; width: 244px; height: 230px; background: linear-gradient(135deg, #8b7d70 0%, #c9b7a3 55%, #4d4a4a 100%); }
  .value-mark { left: 460px; top: 14px; }
  .value-title { left: 387px; top: 60px; color: var(--white); font-size: 19px; line-height: 1.45; }
  .value-text { left: 388px; top: 150px; width: 150px; font-size: 5.6px; line-height: 1.6; color: var(--white); }
  .value-text ul { padding-left: 14px; }

  /* slide 11 */
  .cycle { left: 50px; top: 45px; width: 240px; height: 225px; }
  .place-title { left: 335px; top: 66px; font-size: 20px; }
  .place-list { left: 335px; top: 132px; width: 180px; }
  .place-item { margin-bottom: 10px; }
  .place-item h4 { font-family: "Ubuntu", sans-serif; font-weight: 400; font-size: 8.5px; color: var(--green); margin-bottom: 2px; }
  .place-item p { font-size: 5.5px; line-height: 1.5; color: #333; }

  /* slide 12 */
  .emotional { background: var(--forest); }
  .emo-mark { left: 40px; top: 12px; font-size: 19px; }
  .emo-title { left: 40px; top: 48px; color: var(--white); font-size: 19px; }
  .emo-ring { left: 158px; top: 40px; width: 240px; height: 240px; }
  .emo-item { width: 95px; color: var(--white); }
  .emo-item h4 { font-family: "Ubuntu", sans-serif; font-weight: 400; font-size: 9px; line-height: 1.2; }
  .emo-item p { font-size: 4.6px; line-height: 1.5; margin-top: 3px; }
  .bar.s1 { left: 0; width: 34%; background: var(--green); }
  .bar.s2 { left: 34%; width: 32%; background: var(--lime); }
  .bar.s3 { left: 66%; width: 34%; background: #b7bdd0; }
</style>
</head>
<body>
<div class="board">

  <!-- cover -->
  <section class="slide col-l row1">
    <div class="cover-photo" role="img" aria-label="Photo: businessman sitting by a large office window with a cup"></div>
    <div class="cover-band"></div>
    <div class="cover-title">
      <span class="wordmark">Kelmora</span>
      <span class="product">Bridges2<br>Client<br>Worth</span>
    </div>
    <div class="cover-tag">Presentation to:<br>The Client Name Here</div>
  </section>

  <!-- intro -->
  <section class="slide col-r row1">
    <div class="runner-photo" role="img" aria-label="Photo: woman running on a bridge above a city"></div>
    <div class="wordmark intro-mark">Kelmora</div>
    <p class="small intro-text">Then, think about every level of brand management, which is another way of saying: every point at which consumers interact with your brand. Most people think of social media and website. Then, think about every level of brand management, which is another way of saying: every point at which consumers i</p>
  </section>

  <!-- hello -->
  <section class="slide col-l row2">
    <div class="meeting-photo" role="img" aria-label="Photo: presenter at a flip chart in a meeting room"></div>
    <div class="meeting-tint"></div>
    <div class="meeting-veil"></div>
    <h2 class="hello-title">Hello Kelmora</h2>
    <p class="small hello-text">Then, think about every level of brand management, which is another way of saying: every point at which consumers interact with your brand. Most people think of social media and website. Then, think about every level of brand management, which is another way of saying: every point at which consumers i</p>
    <div class="hello-vertical">Hello Kelmora</div>
  </section>

  <!-- we are -->
  <section class="slide col-r row2">
    <h2 class="heading we-title">We Are Kelmora</h2>
    <div class="we-text">
      <p>We help companies to create, calculate and communicate customer value and capture that value into cashflow. Company owners, boards and management teams will use this platform and the digital tool to have a transparent customer value view. The digital tool helps everyone in the organization to see how they can create value in their job.</p>
      <p>Benefits of Bridges2ClientWorth - tool:<br>Emotional benefits:<br>- Helps me succeed<br>- I’m forerunner<br>- I’m up to date<br>- I accomplish<br>- process is under control<br>- Ease to lead<br>- Ease in communication</p>
    </div>
    <div class="leaf-photo" role="img" aria-label="Photo: close-up of a green leaf"></div>
    <div class="water-photo" role="img" aria-label="Photo: glass sphere on turquoise water"></div>
    <div class="we-band"></div>
    <div class="wordmark light we-mark">Kelmora</div>
    <p class="small light we-note1">We, think about every level of brand</p>
    <p class="small light we-note2">We, think about every level of brand</p>
  </section>

  <!-- quote -->
  <section class="slide col-l row3">
    <div class="hands-photo" role="img" aria-label="Photo: team stacking hands together"></div>
    <div class="quote-band"></div>
    <div class="quote-panel"></div>
    <p class="small light quote-lead">Then, think about every level of brand management, which is another way of saying: every point at which consumers interact with your</p>
    <blockquote class="quote-text">“A <b>brand</b> is no longer what we tell the consumer it is – it is what consumers tell each other it is”</blockquote>
    <div class="wordmark light quote-mark">Kelmora</div>
  </section>

  <!-- profile -->
  <section class="slide col-r row3">
    <div class="wordmark corner-mark">Kelmora</div>
    <h2 class="heading profile-title">Profile Kelmora</h2>
    <p class="small profile-text1">Then, think about every level of brand management, which is another way of saying: every point at which consumers interact with your brand. Most people think of social media and website.</p>
    <p class="small profile-text2">Then, think about every level of brand management, which is another way of saying: every point at which consumers interact with your brand.</p>
    <div class="profile-block"></div>
    <div class="desk-photo" role="img" aria-label="Photo: desk with charts and laptops, green tinted"></div>
  </section>

  <!-- digital tool -->
  <section class="slide col-l row4">
    <div class="tool-block"></div>
    <div class="tool-haze1"></div>
    <div class="tool-haze2"></div>
    <div class="class-photo" role="img" aria-label="Photo: people working at laptops in a bright room"></div>
    <div class="laptop-photo" role="img" aria-label="Photo: laptop on a desk, green tinted"></div>
    <div class="wordmark corner-mark">Kelmora</div>
    <h2 class="heading tool-title">Digital Tool<br>Helps everyone</h2>
    <div class="tool-list">
      <div class="tool-item"><h4>Your Text Here</h4><p class="small">Then, think about every level of brand management,<br>which is another way of saying:</p></div>
      <div class="tool-item"><h4>Your Text Here</h4><p class="small">Then, think about every level of brand management,<br>which is another way of saying:</p></div>
      <div class="tool-item"><h4>Your Text Here</h4><p class="small">Then, think about every level of brand management,<br>which is another way of saying:</p></div>
    </div>
  </section>

  <!-- rational benefits -->
  <section class="slide col-r row4">
    <div class="wordmark corner-mark">Kelmora</div>
    <div class="grey-photo" role="img" aria-label="Photo: hands on a table with a phone, black and white"></div>
    <div class="green-photo" role="img" aria-label="Photo: team around a laptop, green tinted"></div>
    <div class="rational-mint"></div>
    <h2 class="heading rational-title">Rational Benefits:</h2>
    <ul class="rational-list">
      <li>- Simplicity in complex world of value</li>
      <li>- Clarity</li>
      <li>- Easy access - low deployment threshold</li>
    </ul>
  </section>

  <!-- about -->
  <section class="slide col-l row5">
    <div class="about-top"></div>
    <div class="wordmark about-mark">Kelmora</div>
    <div class="circle-photo" role="img" aria-label="Photo: hands linked in a circle"></div>
    <div class="about-bottom"></div>
    <h2 class="heading about-title">About Kelmora</h2>
    <p class="small about-text">Then, think about every level of brand management, which is another way of saying: every point at which consumers interact with your brand. Most people think of social media and website. Then, think about every level of brand management, which is another way of saying: every point at which consumers interact with your brand. Then, think about every level of brand management, which is another way of saying: every point at which consumers interact with your brand. Then, think about every level of brand management, which is another way of saying: every point at which consumers interact with your brand.</p>
  </section>

  <!-- create value -->
  <section class="slide col-r row5">
    <div class="value-mint"></div>
    <div class="value-band"></div>
    <div class="shop-photo" role="img" aria-label="Photo: shop assistant handing a bag to two customers"></div>
    <div class="wordmark light value-mark">Kelmora</div>
    <h2 class="heading value-title">We can<br>create value<br>in their job</h2>
    <div class="value-text">
      <p>Benefits of Bridges2ClientWorth -tool:<br>Emotional benefits:</p>
      <ul>
        <li>Helps me succeed</li><li>I’m forerunner</li><li>I’m up to date</li><li>I accomplish</li>
        <li>Process is under control</li><li>Ease to lead</li><li>Ease in communication</li>
      </ul>
    </div>
  </section>

  <!-- cycle diagram -->
  <section class="slide col-l row6">
    <div class="wordmark corner-mark">Kelmora</div>
    <svg class="cycle" viewBox="0 0 240 225" aria-hidden="true">
      <defs>
        <clipPath id="tri"><path d="M100 18 Q120 -6 140 18 L228 170 Q240 205 205 210 L35 210 Q0 205 12 170 Z"/></clipPath>
      </defs>
      <g clip-path="url(#tri)">
        <polygon points="120,125 -40,-40 280,-40" fill="#a3a3a3"/>
        <polygon points="120,125 -40,-40 -40,260 130,260" fill="#8cd614"/>
        <polygon points="120,125 280,-40 280,260 130,260" fill="#22c31e"/>
      </g>
      <circle cx="120" cy="125" r="52" fill="#fff"/>
      <circle cx="112" cy="40" r="17" fill="#fff"/>
      <path d="M112 31 A9 9 0 1 0 121 40 L112 40 Z" fill="none" stroke="#a3a3a3" stroke-width="2"/>
      <circle cx="37" cy="180" r="17" fill="#fff"/>
      <rect x="28" y="175" width="18" height="12" rx="2" fill="#8cd614"/>
      <rect x="33" y="171" width="8" height="5" rx="1" fill="none" stroke="#8cd614" stroke-width="2"/>
      <circle cx="195" cy="180" r="10" fill="none" stroke="#fff" stroke-width="5" stroke-dasharray="4 3"/>
      <circle cx="195" cy="180" r="4" fill="#fff"/>
    </svg>
    <h2 class="heading place-title">Place your &nbsp;text<br>title here</h2>
    <div class="place-list">
      <div class="place-item"><h4>Simplicity in complex world of value</h4><p>Lorem ipsum dolor sit amet, consectetur adipiscing elit, sed do eiusmod tempor incididunt.</p></div>
      <div class="place-item"><h4>Clarity</h4><p>Lorem ipsum dolor sit amet, consectetur adipiscing elit, sed do eiusmod tempor incididunt.</p></div>
      <div class="place-item"><h4>Easy access - low deployment</h4><p>sit amet, consectetur adipiscing elit, sed do eiusmod tempor incididunt.</p></div>
    </div>
    <div class="bar s1"></div><div class="bar s2"></div><div class="bar s3"></div>
  </section>

  <!-- emotional benefits -->
  <section class="slide col-r row6 emotional">
    <div class="wordmark light emo-mark">Kelmora</div>
    <h2 class="heading emo-title">Emotional benefits:</h2>
    <svg class="emo-ring" viewBox="-120 -120 240 240" aria-hidden="true">
      <polygon points="111,46 46,111 24,57 57,24" fill="#3f9e8c"/>
      <polygon points="46,111 -46,111 -24,57 24,57" fill="#8fd0a4"/>
      <polygon points="-46,111 -111,46 -57,24 -24,57" fill="#b8e6b8"/>
      <polygon points="-111,46 -111,-46 -57,-24 -57,24" fill="#d3f0c8"/>
      <polygon points="-111,-46 -46,-111 -24,-57 -57,-24" fill="#e6f7d8"/>
      <polygon points="-46,-111 46,-111 24,-57 -24,-57" fill="#1b7d1f"/>
      <polygon points="46,-111 111,-46 57,-24 24,-57" fill="#5aa99a"/>
      <polygon points="111,-46 111,46 57,24 57,-24" fill="#4f9f98"/>
      <text x="-8" y="96" font-family="Ubuntu, sans-serif" font-size="22" fill="#fff">$</text>
    </svg>
    <div class="emo-item" style="left:40px;top:103px"><h4>Ease<br>communication</h4><p>Lorem ipsum dolor sit amet, consetur adipin nnscing elit</p></div>
    <div class="emo-item" style="left:40px;top:173px"><h4>Ease to lead</h4><p>Lorem ipsum dolor sit amet, consetur adipin nnscing elit</p></div>
    <div class="emo-item" style="left:40px;top:236px"><h4>Process is under<br>control</h4><p>Lorem ipsum dolor sit amet, consetur adipin nnscing elit</p></div>
    <div class="emo-item" style="left:434px;top:30px"><h4>Helps<br>me succeed</h4><p>Lorem ipsum dolor sit amet, consetur adipin nnscing elit</p></div>
    <div class="emo-item" style="left:435px;top:108px"><h4>I’m forerunner</h4><p>Lorem ipsum dolor sit amet, consetur adipin nnscing elit</p></div>
    <div class="emo-item" style="left:435px;top:172px"><h4>I’m up to date</h4><p>Lorem ipsum dolor sit amet, consetur adipin nnscing elit</p></div>
    <div class="emo-item" style="left:435px;top:236px"><h4>I accomplish</h4><p>Lorem ipsum dolor sit amet, consetur adipin nnscing elit</p></div>
    <div class="bar s1"></div><div class="bar s2"></div><div class="bar s3"></div>
  </section>

</div>
</body>
</html>
```